Cover für Podcast gesucht
Zielgruppe
Wir wollen einen PODCAST Rund um das Thema Business, Digitale Transformation und Tech starten. Unsere Zielgruppe sind Entscheidungsträger*innen die sich über aktuelle Trends, digitale und tech-orientierte Geschäftsmodelle sowie Tools und Management-Methoden auf dem Laufenden halten möchten.
Aufgabenstellung
ACHTUNG: ES HANDELT SICH HIERBEI UM EIN PODCAST COVER: Wir möchten auf dem Cover unsere beiden Fotos, die wir liefern, integriert haben sowie auch einen Schriftzug mit dem Namen 'wolkig verzweigt', der auch künftig als Logo für unsere Website fungieren soll. Das Cover soll das Thema 'digitalisierung', 'innovation', 'technologie / tech' 'trendy' umreißen.
Auf dem Cover sollten die beiden Bilder unserer Personen, der Schriftzug 'wolkig verzweigt' und darunter (subline) Business & Tech Talk stehen.

```html
<!DOCTYPE html>
<html lang="de">
<head>
<meta charset="utf-8">
<title>wolkig verzweigt – Podcast Cover</title>
<link rel="stylesheet" href="https://fonts.googleapis.com/css2?family=Montserrat:wght@300;400;500;800;900&display=swap">
<style>
  :root {
    --sky: #5697d8;
    --sky-deep: #4a86cc;
    --sky-light: #74b0e6;
    --frame-olive: #a4b46a;
    --photo-light: #6f9bb6;
    --photo-dark: #3d6275;
    --sun-yellow: #e9c31a;
    --white: #ffffff;
  }
  * { margin: 0; padding: 0; box-sizing: border-box; }
  html, body { width: 1200px; height: 1200px; overflow: hidden; background: var(--sky); }
  .cover {
    position: relative;
    width: 1200px;
    height: 1200px;
    overflow: hidden;
    background: linear-gradient(160deg, var(--sky-light) 0%, var(--sky) 45%, var(--sky-deep) 100%);
    font-family: "Montserrat", sans-serif;
  }
  .cover-waves, .host-photos { position: absolute; left: 0; top: 0; }
  .accent-frame {
    position: absolute;
    left: 45px; top: 45px;
    width: 1110px; height: 640px;
    border: 12px solid var(--frame-olive);
  }
  .brand-mark {
    position: absolute;
    left: 0; width: 1200px; top: 590px;
    display: flex; justify-content: center; align-items: center; gap: 8px;
    color: var(--white);
    font-weight: 500;
    font-size: 17px;
    white-space: nowrap;
  }
  .brand-mark-dot {
    width: 16px; height: 16px;
    border: 3px solid var(--white);
    border-radius: 50%;
    flex: none;
  }
  .show-title {
    position: absolute;
    left: 0; width: 1212px;
    text-align: center;
    line-height: 1;
  }
  .show-title-main {
    top: 756px;
    color: var(--sun-yellow);
    font-weight: 800;
    font-size: 128px;
    letter-spacing: 1px;
  }
  .show-title-sub {
    top: 900px;
    color: var(--white);
    font-weight: 300;
    font-size: 82px;
    letter-spacing: 2px;
  }
  .show-subline {
    position: absolute;
    left: 0; width: 1212px; top: 1012px;
    text-align: center;
    color: var(--white);
    font-weight: 500;
    font-size: 30px;
    letter-spacing: 4px;
    text-transform: uppercase;
  }
  .host-band {
    position: absolute;
    left: 0; top: 1096px;
    width: 1200px; height: 104px;
    background: var(--sun-yellow);
    color: var(--white);
    font-weight: 800;
    font-size: 40px;
  }
  .host-name, .host-amp {
    position: absolute;
    top: 50%;
    transform: translate(-50%, -50%);
    white-space: nowrap;
  }
  .host-name--left { left: 283px; }
  .host-amp { left: 600px; font-weight: 900; font-size: 60px; }
  .host-name--right { left: 924px; }
</style>
</head>
<body>
  <main class="cover">
    <svg class="cover-waves" width="1200" height="1200" viewBox="0 0 1200 1200" aria-hidden="true">
      <path d="M336 0 C 330 200, 380 420, 700 520 L 1200 520 L 1200 0 Z" fill="#5fa4e0" opacity="0.55"/>
      <path d="M0 140 C 200 90, 450 160, 720 300 C 900 400, 1050 520, 1200 560 L 1200 1200 L 0 1200 Z" fill="#4f8fd2" opacity="0.45"/>
      <path d="M980 0 C 1080 60, 1160 150, 1200 220 L 1200 0 Z" fill="#6bb4e8" opacity="0.5"/>
    </svg>

    <div class="accent-frame"></div>

    <svg class="host-photos" width="1200" height="1200" viewBox="0 0 1200 1200">
      <defs>
        <linearGradient id="photo-tone" x1="0" y1="0" x2="0" y2="1">
          <stop offset="0" stop-color="#3d6275"/>
          <stop offset="0.45" stop-color="#6f9bb6"/>
          <stop offset="1" stop-color="#4a7187"/>
        </linearGradient>
        <linearGradient id="photo-tone-dark" x1="0" y1="0" x2="0" y2="1">
          <stop offset="0" stop-color="#3d6275"/>
          <stop offset="0.4" stop-color="#6a95ad"/>
          <stop offset="1" stop-color="#3d6275"/>
        </linearGradient>
      </defs>
      <path class="host-photo host-photo--left" role="img" aria-label="Portraitfoto des ersten Hosts in Blau-Duoton, kariertes Hemd"
        fill="url(#photo-tone)"
        d="M165 300 C 170 230, 260 200, 350 203 C 450 205, 530 250, 537 340 C 545 420, 525 520, 520 570 C 560 590, 620 610, 650 640 L 650 1096 L 0 1096 L 0 620 C 60 600, 130 590, 185 570 C 170 500, 160 400, 165 300 Z"/>
      <path class="host-photo host-photo--right" role="img" aria-label="Portraitfoto des zweiten Hosts in Blau-Duoton, lächelnd, Steppjacke"
        fill="url(#photo-tone-dark)"
        d="M715 330 C 720 240, 800 197, 890 197 C 990 198, 1060 250, 1067 340 C 1072 400, 1070 450, 1080 490 C 1120 505, 1170 520, 1200 540 L 1200 1096 L 480 1096 C 520 950, 560 780, 640 660 C 680 630, 720 615, 745 600 C 725 520, 712 420, 715 330 Z"/>
    </svg>

    <div class="brand-mark">
      <span class="brand-mark-dot"></span>
      <span class="brand-mark-name">wolkig verzweigt</span>
    </div>

    <h1 class="show-title show-title-main">WOLKIG</h1>
    <p class="show-title show-title-sub">VERZWEIGT</p>
    <p class="show-subline">Business &amp; Tech Talk</p>

    <footer class="host-band">
      <span class="host-name host-name--left">Jonas Brenner</span>
      <span class="host-amp">&amp;</span>
      <span class="host-name host-name--right">Felix Marquardt</span>
    </footer>
  </main>
</body>
</html>
```